Mortgage Loan Program(s) for Furloughed Federal Government Workers

Mortgage Loan Program(s)
For
Furloughed Federal Government Workers

* Preserve Your Credit Rating
* Receive Cash out to Increase Savings or Consolidate Bills
* Close in 30 Days or Less
* FHA and Conventional Loan Programs
* Very Competitive Rates Available
* DC & MD Properties Only

You deserve better. Contact us today....

Office (800) 446-2917 x24
Cell (240) 958-2043
Email mpelton@brightkeyhome.example

Marcus Pelton
Brightkey Financial Services, Inc.
NMLS #518374 / #60471

Target Market(s)

```html
<!DOCTYPE html>
<html lang="en">
<head>
<meta charset="utf-8">
<title>Mortgage Loan Programs for Furloughed Federal Government Workers</title>
<link rel="stylesheet" href="https://fonts.googleapis.com/css2?family=Montserrat:wght@800&family=Open+Sans:wght@400;600;700&family=Roboto+Slab:wght@900&display=swap">
<style>
  :root {
    --blue: #1d5fa8;
    --blue-deep: #174f8f;
    --gold: #ad9d33;
    --gold-text: #c7b03a;
    --ink: #222222;
    --white: #ffffff;
    --stamp: #e0403a;
    --page: #ffffff;
  }
  * { margin: 0; padding: 0; box-sizing: border-box; }
  html, body { width: 1200px; height: 1200px; overflow: hidden; background: var(--page); }
  body { position: relative; font-family: "Open Sans", Arial, sans-serif; color: var(--ink); }

  .flyer {
    position: absolute; left: 46px; top: 182px;
    width: 1114px; height: 840px;
    background: var(--white);
    box-shadow: 2px 3px 6px rgba(0,0,0,0.35);
    overflow: hidden;
  }
  .flyer-shapes { position: absolute; inset: 0; }

  .brand {
    position: absolute; left: 34px; top: 88px; width: 250px;
    display: flex; align-items: center; gap: 12px;
  }
  .brand-dot { width: 34px; height: 34px; flex: none; border-radius: 50%; background: var(--gold); }
  .brand-name { font-weight: 600; font-size: 19px; line-height: 1.2; color: var(--blue); }

  .stamp {
    position: absolute; left: 690px; top: 60px;
    transform: rotate(-10deg);
    border: 5px solid var(--stamp); border-radius: 6px;
    padding: 6px 18px;
    outline: 2px solid var(--stamp); outline-offset: 4px;
    font-family: "Roboto Slab", Georgia, serif; font-weight: 900;
    font-size: 62px; line-height: 1; letter-spacing: 1px;
    color: var(--stamp); opacity: 0.92;
  }

  .tagline {
    position: absolute; left: 38px; top: 452px;
    font-weight: 700; font-size: 33px; line-height: 41px;
    color: var(--white); text-transform: uppercase;
  }

  .headline {
    position: absolute; right: 36px; top: 428px; text-align: right;
    font-family: "Montserrat", Arial, sans-serif; font-weight: 800;
    text-transform: uppercase;
  }
  .headline-kicker { display: block; font-size: 22px; line-height: 26px; color: var(--blue); }
  .headline-main { display: block; font-size: 30px; line-height: 38px; color: var(--white); margin-top: 2px; }

  .features { position: absolute; left: 0; top: 614px; width: 920px; height: 120px; list-style: none; }
  .feature { position: absolute; top: 0; width: 160px; margin-left: -80px; text-align: center; }
  .feature-icon { display: block; width: 56px; height: 56px; margin: 0 auto; background: var(--gold); }
  .feature-label { display: block; margin-top: 17px; font-size: 14px; line-height: 18px; color: var(--ink); }
  .feature:nth-child(2) .feature-label { margin-top: 13px; }

  .agent-photo {
    position: absolute; left: 926px; top: 562px; width: 188px; height: 192px;
    background: linear-gradient(180deg, #f4f4f4 0%, #d9d4cf 45%, #2a2a2c 80%, #1d1d1f 100%);
  }

  .footer {
    position: absolute; left: 0; top: 754px; width: 1114px; height: 86px;
    background: var(--blue); color: var(--white);
  }
  .footer-cta {
    position: absolute; left: 25px; top: 11px;
    font-weight: 700; font-size: 21px; line-height: 24px; color: var(--gold-text);
    text-transform: uppercase;
  }
  .footer-contact { position: absolute; left: 25px; top: 36px; font-size: 14px; line-height: 18px; }
  .footer-agent { position: absolute; right: 19px; top: 18px; text-align: right; }
  .agent-name { font-size: 21px; line-height: 24px; text-transform: uppercase; }
  .agent-meta { font-size: 13px; line-height: 18px; }
  .sep { margin: 0 10px; }
</style>
</head>
<body>
<main class="flyer">
  <svg class="flyer-shapes" width="1114" height="840" viewBox="0 0 1114 840" aria-hidden="false">
    <!-- hero photo area -->
    <rect role="img" aria-label="Photo of the Capitol building at dusk under a deep blue sky" x="0" y="0" width="1114" height="560" fill="url(#heroTone)"/>
    <defs>
      <linearGradient id="heroTone" x1="0" y1="0" x2="0" y2="1">
        <stop offset="0" stop-color="#1e4f9c"/>
        <stop offset="0.45" stop-color="#4f84c6"/>
        <stop offset="0.62" stop-color="#7a5a3e"/>
        <stop offset="0.85" stop-color="#3a2a22"/>
        <stop offset="1" stop-color="#241c1a"/>
      </linearGradient>
    </defs>
    <!-- logo panel -->
    <polygon points="0,0 389,0 322,202 0,202" fill="var(--white)"/>
    <polyline points="389,0 322,202 0,202" fill="none" stroke="var(--gold)" stroke-width="3"/>
    <!-- lower white area -->
    <polygon points="0,546 286,569 393,528 1114,546 1114,840 0,840" fill="var(--white)"/>
    <!-- blue band -->
    <polygon points="0,358 390,526 286,569 0,546" fill="var(--blue)"/>
    <!-- white accent stripe -->
    <polygon points="393,528 492,440 1114,340 1114,350 496,450" fill="var(--white)"/>
    <!-- gold band -->
    <polygon points="393,528 496,450 1114,350 1114,546" fill="var(--gold)"/>
  </svg>

  <div class="brand">
    <span class="brand-dot"></span>
    <span class="brand-name">Brightkey Financial Services, Inc.</span>
  </div>

  <div class="stamp">APPROVED</div>

  <h2 class="tagline">You<br>Deserve Better</h2>

  <h1 class="headline">
    <span class="headline-kicker">Mortgage Loan Programs For</span>
    <span class="headline-main">Furloughed Federal<br>Government Workers</span>
  </h1>

  <ul class="features">
    <li class="feature" style="left:82px">
      <svg class="feature-icon" viewBox="0 0 56 56" fill="none" stroke="#fff" stroke-width="1.8">
        <path d="M10 34 A18 18 0 0 1 46 34 Z"/><path d="M28 34 L38 22"/><path d="M16 34 A12 12 0 0 1 40 34"/>
        <rect x="9" y="38" width="38" height="9"/><path d="M14 42.5h4M22 42.5h4M30 42.5h4M38 42.5h4"/>
      </svg>
      <span class="feature-label">Preserve Your<br>Credit Rating</span>
    </li>
    <li class="feature" style="left:212px">
      <svg class="feature-icon" viewBox="0 0 56 56" fill="none" stroke="#fff" stroke-width="1.8">
        <rect x="20" y="6" width="20" height="30" fill="#fff"/><circle cx="30" cy="20" r="4" stroke="var(--gold)"/>
        <path d="M10 34h8l10 4h10v6H24l-14-2z" fill="#fff"/><path d="M6 32h6v16H6z" fill="#fff"/>
      </svg>
      <span class="feature-label">Receive Cash out to<br>Increase Savings or<br>Consolidate Bills</span>
    </li>
    <li class="feature" style="left:349px">
      <svg class="feature-icon" viewBox="0 0 56 56" fill="none" stroke="#fff" stroke-width="1.8">
        <rect x="9" y="12" width="32" height="28" rx="2"/><path d="M9 19h32M16 8v7M34 8v7"/>
        <path d="M15 25h4M23 25h4M31 25h4M15 31h4M23 31h4"/>
        <circle cx="40" cy="40" r="8" fill="var(--gold)"/><path d="M36 40l3 3 5-6"/>
      </svg>
      <span class="feature-label">Close in 30 Days<br>or Less</span>
    </li>
    <li class="feature" style="left:497px">
      <svg class="feature-icon" viewBox="0 0 56 56" fill="none" stroke="#fff" stroke-width="1.8">
        <path d="M22 12c-6 4-8 10-8 14a10 10 0 0 0 20 0c0-4-2-10-8-14z" fill="#fff"/>
        <path d="M24 20v14M21 24c0-2 6-2 6 0s-6 2-6 5 6 3 6 0" stroke="var(--gold)"/>
        <path d="M18 46h10l12-5 4 2-14 7H18z" fill="#fff"/><path d="M44 42h6v8h-6z" fill="#fff"/>
      </svg>
      <span class="feature-label">FHA and Conventional<br>Loan Programs</span>
    </li>
    <li class="feature" style="left:668px">
      <svg class="feature-icon" viewBox="0 0 56 56" fill="#fff" stroke="none">
        <rect x="10" y="36" width="6" height="10"/><rect x="19" y="30" width="6" height="16"/>
        <rect x="28" y="24" width="6" height="22"/><rect x="37" y="16" width="6" height="30"/>
        <path d="M10 30 L22 22 L30 24 L42 12" fill="none" stroke="#fff" stroke-width="1.8"/>
        <path d="M38 11h6v6z"/>
      </svg>
      <span class="feature-label">Very Competitive Rates<br>Available</span>
    </li>
    <li class="feature" style="left:832px">
      <svg class="feature-icon" viewBox="0 0 56 56" fill="none" stroke="#fff" stroke-width="1.8">
        <path d="M8 22 L28 8 L48 22"/><rect x="12" y="22" width="32" height="24"/>
        <circle cx="28" cy="17" r="3"/><rect x="16" y="27" width="6" height="6"/><rect x="34" y="27" width="6" height="6"/>
        <rect x="24" y="34" width="8" height="12"/><rect x="16" y="37" width="6" height="6"/><rect x="34" y="37" width="6" height="6"/>
      </svg>
      <span class="feature-label">DC &amp; MD Properties<br>Only</span>
    </li>
  </ul>

  <div class="agent-photo" role="img" aria-label="Portrait photo of the loan officer in a dark suit and tie"></div>

  <footer class="footer">
    <p class="footer-cta">Contact Us Today</p>
    <p class="footer-contact">
      Office: (800) 446-2917 x24<span class="sep">I</span>Cell: (240) 958-2043<br>
      Email: mpelton@brightkeyhome.example
    </p>
    <div class="footer-agent">
      <p class="agent-name">Marcus Pelton</p>
      <p class="agent-meta">Brightkey Financial Services, Inc.<span class="sep">I</span>NMLS #518374 / #60471</p>
    </div>
  </footer>
</main>
</body>
</html>
```